Brivond Technologies business card design

We need a business card designed with our new logo. it would be great if the card could communicate it is a technology based company.

Target Market(s)

system integrators

Industry/Entity Type

technology, IOT

Contact Information for Business Card

Name, designation, Address, telephone number, email address

Requirements
Must have
• logo and company name
Nice to have
• something to do with technology

```html
<!DOCTYPE html>
<html lang="en">
<head>
<meta charset="utf-8">
<title>Brivond Technologies – Business Card</title>
<link href="https://fonts.googleapis.com/css2?family=Arimo:wght@400&family=Montserrat:wght@500;700&display=swap" rel="stylesheet">
<style>
  :root {
    --bg: #d7d7d7;
    --card-light: #ffffff;
    --card-dark: #3a393b;
    --ink: #3a393b;
    --orange: #f7941d;
    --divider: #d9d9d9;
  }
  * { margin: 0; padding: 0; box-sizing: border-box; }
  html, body { width: 1075px; height: 1200px; overflow: hidden; }
  body { background: var(--bg); position: relative; font-family: "Arimo", Arial, sans-serif; }

  .card { position: absolute; left: 206px; width: 665px; height: 395px; overflow: hidden; }
  .card--front { top: 187px; background: var(--card-light); }
  .card--back { top: 637px; background: var(--card-dark); }

  .corner { position: absolute; }
  .corner--top { left: 0; top: 0; width: 155px; height: 125px;
    background: linear-gradient(135deg, var(--orange) 0%, rgba(247,148,29,0.55) 45%, rgba(247,148,29,0) 75%); }
  .corner--bottom { right: 0; bottom: 0; width: 160px; height: 105px;
    background: linear-gradient(315deg, var(--orange) 0%, rgba(247,148,29,0.55) 45%, rgba(247,148,29,0) 75%); }

  .brand { position: absolute; display: flex; align-items: center; gap: 14px;
    font-family: "Montserrat", sans-serif; font-weight: 700; letter-spacing: 0.5px; white-space: nowrap; }
  .brand__square { background: var(--orange); flex: none; }
  .brand__name { line-height: 1.1; }
  .brand--front { left: 36px; top: 168px; font-size: 27px; color: var(--ink); }
  .brand--front .brand__square { width: 22px; height: 22px; }
  .brand--back { left: 0; right: 0; top: 172px; justify-content: center; font-size: 40px; color: #ffffff; }
  .brand--back .brand__square { width: 30px; height: 30px; }

  .divider { position: absolute; left: 344px; top: 101px; width: 1px; height: 193px; background: var(--divider); }

  .contact { position: absolute; left: 370px; top: 95px; color: var(--ink); }
  .contact__name { font-family: "Montserrat", sans-serif; font-weight: 700; font-size: 25px; line-height: 1; letter-spacing: 0.2px; }
  .contact__role { color: var(--orange); font-size: 17px; margin-top: 3px; }
  .contact__list { list-style: none; margin-top: 18px; font-size: 18px; }
  .contact__list li { display: flex; align-items: center; gap: 8px; height: 24px; }
  .contact__list svg { width: 16px; height: 16px; flex: none; }
  .contact__address { font-size: 18px; line-height: 24px; margin-top: 18px; }
</style>
</head>
<body>

<section class="card card--front">
  <div class="corner corner--top" role="img" aria-label="Orange and charcoal pixel block decoration"></div>
  <div class="corner corner--bottom" role="img" aria-label="Orange and charcoal pixel block decoration"></div>

  <div class="brand brand--front"><span class="brand__square"></span><span class="brand__name">Brivond<br>Technologies</span></div>

  <div class="divider"></div>

  <div class="contact">
    <p class="contact__name">MARCUS HALE</p>
    <p class="contact__role">Managing Director</p>
    <ul class="contact__list">
      <li>
        <svg viewBox="0 0 16 16" aria-hidden="true"><path d="M3 1.5l3 .5 1 3.2-1.8 1.3a9 9 0 0 0 4.3 4.3L10.8 9l3.2 1 .5 3c-.5 1-1.5 1.5-2.5 1.5C6.5 14.5 1.5 9.5 1.5 4c0-1 .5-2 1.5-2.5z" fill="none" stroke="var(--orange)" stroke-width="1.6"/></svg>
        044-987 654 321
      </li>
      <li>
        <svg viewBox="0 0 16 16" aria-hidden="true"><rect x="1" y="3" width="14" height="10" fill="var(--orange)"/><path d="M1 3l7 6 7-6" fill="none" stroke="#fff" stroke-width="1.3"/></svg>
        info@brivondtech.com
      </li>
      <li>
        <svg viewBox="0 0 16 16" aria-hidden="true"><g fill="none" stroke="var(--orange)" stroke-width="1.3"><circle cx="8" cy="8" r="6.5"/><ellipse cx="8" cy="8" rx="3" ry="6.5"/><path d="M1.5 8h13M2.5 4.8h11M2.5 11.2h11"/></g></svg>
        www.brivondtech.com
      </li>
    </ul>
    <p class="contact__address">421, Address line goes here<br>45452,Country Name</p>
  </div>
</section>

<section class="card card--back">
  <div class="corner corner--top" role="img" aria-label="Orange pixel block decoration"></div>
  <div class="corner corner--bottom" role="img" aria-label="Orange pixel block decoration"></div>

  <div class="brand brand--back"><span class="brand__square"></span><span class="brand__name">Brivond Technologies</span></div>
</section>

</body>
</html>
```